Film Poster Vorlagen
hallo,
wir benötigen filmposter vorlagen von bekannten oder fiktiven filmen.
die poster werden als vorlagen verwenden.
größe a1
normale kundenfotos sollen nachträglich "einfach/schnell" eingefügt werden können.
wir benötigen ein film poster flair.
beispiele siehe anhang -> original foto + ergebnis.
jedoch sollten unsere vorlagen nicht so nah am original erstellt werden ( copyright! ).
wir freuen uns auf die ergebnisse.
wichtig - als vorlage bitte verwenen anhang ; mg9954 oder mg9525
folgeaufträge - > wir benötigen weitere 9 vorlagen.

```html
<!DOCTYPE html>
<html lang="de">
<head>
<meta charset="utf-8">
<title>Die Wahrheit liegt zwischen den Zeilen – Filmposter</title>
<link rel="stylesheet" href="https://fonts.googleapis.com/css2?family=Roboto+Condensed:wght@700&family=Arimo:wght@700&display=swap">
<style>
  :root {
    --ink-bg: #050507;
    --type-light: #f2f0f8;
    --headline-yellow: #f7b500;
    --headline-box: #000000;
    --skin-warm: #c8926a;
    --skin-light: #e7b897;
    --hair-dark: #3b2a22;
    --field-lavender: #d7d3e6;
  }
  html, body {
    margin: 0;
    padding: 0;
    overflow: hidden;
    background: var(--ink-bg);
  }
  .poster {
    position: relative;
    width: 848px;
    height: 1200px;
    overflow: hidden;
    background: var(--ink-bg);
  }
  .text-field {
    position: absolute;
    left: -500px;
    top: -520px;
    width: 1900px;
    transform: rotate(20deg);
    transform-origin: 950px 1100px;
    font-family: "Roboto Condensed", "Arial Narrow", sans-serif;
    font-weight: 700;
    font-size: 29px;
    line-height: 30px;
    letter-spacing: -0.3px;
    color: var(--type-light);
    text-transform: uppercase;
    white-space: nowrap;
  }
  .text-field p { margin: 0; }
  .portrait-tone {
    position: absolute;
    inset: 0;
    width: 848px;
    height: 1200px;
    mix-blend-mode: multiply;
  }
  .headline {
    position: absolute;
    left: 388px;
    top: 752px;
    transform: rotate(20deg);
    transform-origin: 0 0;
    font-family: "Arimo", Arial, sans-serif;
    font-weight: 700;
    font-size: 40px;
    line-height: 44px;
    color: var(--headline-yellow);
    text-transform: uppercase;
    margin: 0;
  }
  .headline span {
    display: inline-block;
    background: var(--headline-box);
    padding: 0 6px;
    white-space: nowrap;
  }
</style>
</head>
<body>
<main class="poster">
  <div class="text-field" aria-hidden="true">
    <p>Lorem ipsum dolor sit amet consetetur sadipscing elitr sed diam nonumy eirmod tempor invidunt ut labore et dolore magna aliquyam erat sed diam voluptua at vero eos</p>
    <p>Et accusam et justo duo dolores et ea rebum stet clita kasd gubergren no sea takimata sanctus est lorem ipsum dolor sit amet lorem ipsum dolor sit amet consetetur</p>
    <p>Duis autem vel eum iriure dolor in hendrerit in vulputate velit esse molestie consequat vel illum dolore eu feugiat nulla facilisis at vero eros et accumsan et iusto</p>
    <p>Odio dignissim qui blandit praesent luptatum zzril delenit augue duis dolore te feugait nulla facilisi lorem ipsum dolor sit amet consectetuer adipiscing elit sed diam</p>
    <p>Nonummy nibh euismod tincidunt ut laoreet dolore magna aliquam erat volutpat ut wisi enim ad minim veniam quis nostrud exerci tation ullamcorper suscipit lobortis nisl</p>
    <p>Ut aliquip ex ea commodo consequat nam liber tempor cum soluta nobis eleifend option congue nihil imperdiet doming id quod mazim placerat facer possim assum lorem</p>
    <p>Sanctus sea sed takimata ut vero voluptua est lorem ipsum dolor sit amet stet clita kasd gubergren no sea takimata sanctus est lorem ipsum dolor sit amet at vero eos</p>
    <p>Magna qui blandit praesent ulputate lobortis nisl ut aliquip ex ea commodo consequat vero eos et accusam et justo duo dolores et ea rebum stet clita kasd gubergren</p>
    <p>Accumsan et iusto velit nisl ut aliquip facilisi nam liber odio dignissim qui blandit praesent luptatum zzril delenit augue duis dolore te feugait nulla facilisi</p>
    <p>Placerat facer possim assum lorem ipsum dolor sit amet consectetuer adipiscing elit sed diam nonummy nibh euismod tincidunt ut laoreet dolore magna aliquam erat</p>
    <p>Nostrud exerci tation ullamcorper eum iriure dolor in hendrerit in vulputate velit esse molestie consequat vel illum dolore eu feugiat nulla facilisis at vero eros</p>
    <p>Facilisis at vero eros et accumsan dolor sit amet consetetur sadipscing elitr sed diam nonumy eirmod tempor invidunt ut labore et dolore magna aliquyam erat sed</p>
    <p>Accusam et justo duo dolores et ea rebum stet clita kasd gubergren no sea takimata sanctus est lorem ipsum dolor sit amet lorem ipsum dolor sit amet consetetur elitr</p>
    <p>Diam eirmod tempor invidunt ut labore et dolore magna aliquyam erat sed diam voluptua at vero eos et accusam et justo duo dolores et ea rebum stet clita kasd gubergren</p>
    <p>Kasd gubergren no sea takimata sanctus est lorem ipsum dolor sit amet lorem ipsum dolor sit amet consetetur sadipscing elitr sed diam nonumy eirmod tempor invidunt</p>
    <p>Dolor sit amet stet clita ea et gubergren dolores duo eirmod tempor invidunt ut labore et dolore magna aliquyam erat sed diam voluptua at vero eos et accusam et justo</p>
    <p>Invidunt ut labore lorem ipsum dolor sit amet consetetur sadipscing elitr sed diam nonumy sanctus est lorem ipsum dolor sit amet at vero eos et accusam et justo duo</p>
    <p>Dolores et ea rebum stet clita kasd gubergren no sea takimata sanctus est lorem ipsum dolor sit amet consetetur sadipscing elitr sed diam nonumy eirmod tempor ut</p>
    <p>Labore et dolore magna aliquyam erat sed diam voluptua at vero eos et accusam et justo duo dolores et ea rebum stet clita kasd gubergren no sea takimata sanctus est</p>
    <p>Consetetur sadipscing elitr sed diam nonumy eirmod tempor invidunt ut labore et dolore magna aliquyam erat sed diam voluptua at vero eos et accusam et justo duo dolores</p>
    <p>Est lorem ipsum dolor sit amet consetetur sadipscing elitr sed diam nonumy eirmod tempor invidunt ut labore et dolore magna aliquyam erat sed diam voluptua at vero</p>
    <p>Ut labore et dolore magna aliquyam erat sed diam voluptua at vero eos et accusam et justo duo dolores et ea rebum stet clita kasd gubergren no sea takimata sanctus</p>
    <p>Voluptua at vero eos et accusam dolor sit amet dolor sit amet consetetur sadipscing elitr sed diam nonumy eirmod tempor invidunt ut labore et dolore magna aliquyam</p>
    <p>Takimata sanctus est lorem ipsum dolor sit amet dolor sit amet consetetur sadipscing elitr sed diam nonumy eirmod tempor invidunt ut labore et dolore magna aliquyam erat</p>
    <p>Sed diam voluptua at vero eos et accusam et justo duo dolores et ea rebum stet clita kasd gubergren no sea takimata sanctus est lorem ipsum dolor sit amet lorem ipsum</p>
    <p>Vel eum iriure dolor in hendrerit in vulputate velit esse molestie consequat vel illum dolore eu feugiat nulla facilisis at vero eros et accumsan et iusto odio dignissim</p>
    <p>Qui blandit praesent luptatum zzril delenit augue duis dolore te feugait nulla facilisi lorem ipsum dolor sit amet consectetuer adipiscing elit sed diam nonummy nibh</p>
    <p>Euismod tincidunt ut laoreet dolore magna aliquam erat volutpat ut wisi enim ad minim veniam quis nostrud exerci tation ullamcorper suscipit lobortis nisl ut aliquip</p>
    <p>Ex ea commodo consequat duis autem vel eum iriure dolor in hendrerit in vulputate velit esse molestie consequat vel illum dolore eu feugiat nulla facilisis at vero</p>
    <p>Eros et accumsan et iusto odio dignissim qui blandit praesent luptatum zzril delenit augue duis dolore te feugait nulla facilisi nam liber tempor cum soluta nobis</p>
    <p>Eleifend option congue nihil imperdiet doming id quod mazim placerat facer possim assum lorem ipsum dolor sit amet consectetuer adipiscing elit sed diam nonummy nibh</p>
    <p>Tincidunt ut laoreet dolore magna aliquam erat volutpat ut wisi enim ad minim veniam quis nostrud exerci tation ullamcorper suscipit lobortis nisl ut aliquip ex ea</p>
    <p>Commodo consequat sed diam nonummy nibh euismod minim veniam quis nostrud feugiat nulla facilisis at vero eros et accumsan et iusto odio dignissim qui blandit praesent</p>
    <p>Luptatum zzril delenit augue duis dolore te feugait nulla facilisi lorem ipsum dolor sit amet consectetuer adipiscing elit sed diam nonummy nibh euismod tincidunt ut</p>
    <p>Amet clita kasd dolore eu duis autem vel eum iriure dolor in hendrerit in vulputate velit esse molestie consequat vel illum dolore eu feugiat nulla facilisis at vero</p>
    <p>Aliquyam erat consetetur sadipscing elitr sed diam nonumy eirmod tempor invidunt ut labore et dolore magna aliquyam erat sed diam voluptua at vero eos et accusam et</p>
    <p>Gubergren sed diam voluptua sadipscing no sea takimata sanctus est lorem ipsum dolor sit amet lorem ipsum dolor sit amet consetetur sadipscing elitr sed diam nonumy</p>
    <p>Tempor et et invidunt ut labore et dolore magna aliquyam erat sed diam voluptua at vero eos et accusam et justo duo dolores et ea rebum stet clita kasd gubergren sea</p>
    <p>Sadipscing elitr sed diam nonumy eirmod tempor invidunt ut labore et dolore magna aliquyam erat sed diam voluptua at vero eos et accusam et justo duo dolores et ea</p>
    <p>Rebum stet clita kasd gubergren no sea takimata sanctus est lorem ipsum dolor sit amet lorem ipsum dolor sit amet consetetur sadipscing elitr sed diam nonumy eirmod</p>
    <p>Invidunt ut labore et dolore magna aliquyam erat sed diam voluptua at vero eos et accusam et justo duo dolores et ea rebum stet clita kasd gubergren no sea takimata</p>
    <p>Sanctus est lorem ipsum dolor sit amet duis autem vel eum iriure dolor in hendrerit in vulputate velit esse molestie consequat vel illum dolore eu feugiat nulla facilisis</p>
    <p>At vero eros et accumsan et iusto odio dignissim qui blandit praesent luptatum zzril delenit augue duis dolore te feugait nulla facilisi lorem ipsum dolor sit amet</p>
    <p>Consectetuer adipiscing elit sed diam nonummy nibh euismod tincidunt ut laoreet dolore magna aliquam erat volutpat ut wisi enim ad minim veniam quis nostrud exerci</p>
    <p>Tation ullamcorper suscipit lobortis nisl ut aliquip ex ea commodo consequat duis autem vel eum iriure dolor in hendrerit in vulputate velit esse molestie consequat</p>
    <p>Vel illum dolore eu feugiat nulla facilisis at vero eros et accumsan et iusto odio dignissim qui blandit praesent luptatum zzril delenit augue duis dolore te feugait</p>
    <p>Nulla facilisi nam liber tempor cum soluta nobis eleifend option congue nihil imperdiet doming id quod mazim placerat facer possim assum lorem ipsum dolor sit amet</p>
    <p>Consetetur sadipscing elitr sed diam nonumy eirmod tempor invidunt ut labore et dolore magna aliquyam erat sed diam voluptua at vero eos et accusam et justo duo dolores</p>
    <p>Et ea rebum stet clita kasd gubergren no sea takimata sanctus est lorem ipsum dolor sit amet lorem ipsum dolor sit amet consetetur sadipscing elitr sed diam nonumy</p>
    <p>Eirmod tempor invidunt ut labore et dolore magna aliquyam erat sed diam voluptua at vero eos et accusam et justo duo dolores et ea rebum stet clita kasd gubergren no</p>
    <p>Sea takimata sanctus est lorem ipsum dolor sit amet duis autem vel eum iriure dolor in hendrerit in vulputate velit esse molestie consequat vel illum dolore eu feugiat</p>
    <p>Nulla facilisis at vero eros et accumsan et iusto odio dignissim qui blandit praesent luptatum zzril delenit augue duis dolore te feugait nulla facilisi lorem ipsum</p>
    <p>Dolor sit amet consectetuer adipiscing elit sed diam nonummy nibh euismod tincidunt ut laoreet dolore magna aliquam erat volutpat ut wisi enim ad minim veniam quis</p>
    <p>Nostrud exerci tation ullamcorper suscipit lobortis nisl ut aliquip ex ea commodo consequat lorem ipsum dolor sit amet consetetur sadipscing elitr sed diam nonumy</p>
  </div>

  <svg class="portrait-tone" viewBox="0 0 848 1200" role="img" aria-label="Platz für das Kundenfoto: Porträt einer Frau, das durch die Textzeilen hindurchscheint">
    <defs>
      <filter id="soft" x="-30%" y="-30%" width="160%" height="160%">
        <feGaussianBlur stdDeviation="60"/>
      </filter>
    </defs>
    <rect width="848" height="1200" fill="var(--field-lavender)"/>
    <g filter="url(#soft)">
      <ellipse cx="110" cy="820" rx="260" ry="420" fill="var(--skin-warm)"/>
      <ellipse cx="480" cy="900" rx="300" ry="300" fill="var(--skin-warm)"/>
      <ellipse cx="660" cy="740" rx="140" ry="120" fill="var(--skin-light)"/>
      <ellipse cx="330" cy="330" rx="210" ry="260" fill="var(--skin-light)"/>
      <ellipse cx="330" cy="60" rx="240" ry="110" fill="var(--hair-dark)"/>
      <ellipse cx="560" cy="300" rx="70" ry="220" fill="var(--hair-dark)"/>
      <ellipse cx="280" cy="700" rx="200" ry="120" fill="var(--skin-warm)"/>
    </g>
  </svg>

  <h1 class="headline">
    <span>Die Wahrheit liegt</span><br>
    <span>zwischen den Zeilen</span>
  </h1>
</main>
</body>
</html>
```